sailbuddies Website for children with diabilities

Hi, we are looking for a new website design for our community service "sailbuddies". Sailbuddies gives children who suffer from diseases or disabilities a week off on a Boat to give the children new hope and an unforgettable experience.

The current website is really old and we want to have a new one.
Please feel free to discover our website under http://sailbuddies-example.at/.
We have several company sponsors which are very important to us.

The Website has to be a Bootstrap Design (Version 4.4 or higher) [NOT Wordpress, Joomla, other CMS]

Target Market(s)

no target market. we like to inform our communities about our service.

Industry/Entity Type

community service for children with disabilities

Coding

Coded - Design and coding required

Number of Pages Required

4 page

Font styles to use
Sans Serif

Colors
0054AA
0677BA
7BADD7
CADEEF
E8F1F8
0094D4
00A9DD
6FCCEA
C7EBF8
E9F6FB

Requirements
Must have
• About, Sponsors, Information about cruises
Nice to have
• Gallery

```html
<!DOCTYPE html>
<html lang="en">
<head>
<meta charset="utf-8">
<title>Sailbuddies</title>
<link href="https://fonts.googleapis.com/css2?family=Montserrat:wght@400;500;600;700&display=swap" rel="stylesheet">
<style>
:root{
  --navy:#25256b;
  --footer:#1b1a5c;
  --cyan:#00a9dd;
  --sky:#0094d4;
  --pale:#e8f1f8;
  --light:#c7ebf8;
  --text:#555a66;
  --white:#fff;
}
*{margin:0;padding:0;box-sizing:border-box}
html,body{width:1200px;height:3940px;overflow:hidden;background:var(--white)}
body{position:relative;font-family:'Montserrat',sans-serif;color:var(--text)}
.abs{position:absolute}
.btn{position:absolute;display:flex;align-items:center;justify-content:center;border-radius:30px;background:var(--cyan);color:var(--white);font-weight:600;font-size:17px;text-transform:uppercase;text-decoration:none}
.section-title{color:var(--navy);font-weight:700;text-transform:uppercase;line-height:1.25}

/* header */
.topline{right:112px;top:20px;font-size:15px;color:#444}
.topline b{font-weight:600;color:#222}
.nav{right:112px;top:63px;display:flex;gap:26px;font-size:17px;font-weight:500;color:#222}
.brand{left:112px;top:14px;width:138px;height:138px;border-radius:50%;background:var(--navy);z-index:3;display:flex;align-items:center;justify-content:center;color:var(--white);font-weight:700;font-size:17px}

/* hero */
.hero-photo{left:0;top:104px;width:1200px;height:690px;background:linear-gradient(180deg,#8fc3e8 0%,#5c97c9 12%,#1b5fa6 20%,#0b4c94 55%,#0a56a4 100%)}
.hero-waves{left:0;top:560px}
.hero-title{left:108px;top:342px;font-size:58px;font-weight:700;color:var(--white)}
.hero-text{left:112px;top:430px;width:520px;font-size:20px;line-height:31px;color:var(--white)}
.hero-btn{left:112px;top:566px;width:220px;height:58px;background:var(--white);color:#222;font-size:20px;font-weight:500}
.arrow{top:395px;width:24px;height:30px}

/* welcome */
.welcome-photo{left:112px;top:822px;width:423px;height:362px;border-radius:0 46px 0 0;background:linear-gradient(135deg,#c9a06a,#e7c27a 35%,#f1eee8 60%,#9aa4ad)}
.welcome-title{left:625px;top:822px;font-size:42px}
.welcome-text{left:625px;top:946px;width:465px;font-size:16px;line-height:26.5px}
.welcome-btn{left:622px;top:1137px;width:152px;height:48px}

/* sponsors */
.sponsor-band{left:0;top:1240px}
.sponsor-title{left:112px;top:1470px;font-size:40px}
.sponsor-btn{left:112px;top:1607px;width:151px;height:48px}
.sponsor-grid{left:428px;top:1389px;display:grid;grid-template-columns:repeat(3,208px);grid-auto-rows:107px;column-gap:18px;row-gap:19px}
.sponsor-card{background:var(--white);border-radius:10px;box-shadow:0 2px 8px rgba(0,40,90,.08);display:flex;align-items:center;justify-content:center;font-size:18px;font-weight:700;color:var(--navy)}

/* fleet */
.fleet-photo{left:0;top:1826px;width:1200px;height:631px;background:linear-gradient(180deg,#2c6fb1 0%,#4b88c0 35%,#1b5a9c 58%,#0d4f92 100%)}
.fleet-title{left:558px;top:1930px;font-size:40px;color:var(--white)}
.fleet-lead{left:562px;top:2005px;width:520px;font-size:22px;line-height:33px;font-weight:600;color:var(--white)}
.fleet-text{left:566px;top:2100px;width:510px;font-size:16px;line-height:27.5px;color:#e6eef8}
.fleet-btn{left:566px;top:2278px;width:152px;height:48px}

/* gallery */
.gallery-title{left:0;width:1200px;top:2545px;text-align:center;font-size:40px}
.gallery-grid{left:112px;top:2632px;display:grid;grid-template-columns:repeat(3,315px);grid-auto-rows:308px;gap:16px}
.gallery-item{border-radius:0 0 0 0}
.g1{background:linear-gradient(160deg,#9fc7d9,#6db04f 55%,#3e8a3a)}
.g2{background:linear-gradient(160deg,#c9d1d8,#e89a3a 55%,#3d6f95)}
.g3{background:linear-gradient(160deg,#8fa9b8,#d9dde0 50%,#2f5c86)}
.g4{background:linear-gradient(160deg,#c9a9c4,#6d9ad0 50%,#1d4f86)}
.g5{background:linear-gradient(160deg,#2a4a66,#c8ccd0 50%,#1e3c5a)}
.g6{background:linear-gradient(160deg,#b4c3cf,#d8b4a8 50%,#8d6a5c)}
.gallery-btn{left:525px;top:3334px;width:151px;height:48px}

/* footer */
.footer-waves{left:0;top:3340px}
.footer-brand{left:112px;top:3570px;width:220px;height:220px;display:flex;align-items:center;gap:12px;color:var(--white);font-size:24px;font-weight:700}
.footer-brand span.dot{width:40px;height:40px;border-radius:50%;background:var(--white);display:block}
.footer-col{top:3578px;color:var(--white);font-size:16px}
.footer-col h3{font-size:17px;font-weight:600;margin-bottom:22px}
.footer-col li{list-style:none;line-height:31px}
.quick{left:437px}
.contact{left:702px}
.contact li{display:flex;gap:8px;align-items:flex-start;line-height:31px}
.contact li+li{margin-top:31px}
.contact svg{flex:none;margin-top:9px}
.footer-rule{left:112px;top:3832px;width:976px;height:1px;background:rgba(255,255,255,.35)}
.copyright{left:112px;top:3875px;font-size:16px;color:var(--white)}
.social{left:882px;top:3863px;display:flex;gap:12px}
.social span{width:44px;height:44px;border-radius:50%;border:1.5px solid var(--cyan);display:flex;align-items:center;justify-content:center}
</style>
</head>
<body>

<header>
  <div class="abs brand">Sailbuddies</div>
  <p class="abs topline">Registered association ZVR number: <b>000417725</b></p>
  <nav class="abs nav"><span>About</span><span>Sponsors</span><span>Fleet information 2022</span><span>Gallery</span><span>Contact</span></nav>
</header>

<section class="hero">
  <div class="abs hero-photo" role="img" aria-label="Sailboat with a blue and white sail on a deep blue sea, hills on the horizon"></div>
  <svg class="abs hero-waves" width="1200" height="250" viewBox="0 560 1200 250">
    <path d="M0,595 C180,760 480,770 760,705 C960,660 1110,720 1200,795 L1200,810 L0,810Z" fill="#c7ebf8"/>
    <path d="M0,615 C180,760 480,765 760,715 C960,675 1110,730 1200,800" fill="none" stroke="#00a9dd" stroke-width="10"/>
    <path d="M0,650 C200,770 480,780 760,730 C960,700 1110,745 1200,805 L1200,810 L0,810Z" fill="#fff"/>
  </svg>
  <svg class="abs arrow" style="left:44px" viewBox="0 0 24 30"><path d="M16,5 L7,15 L16,25" fill="none" stroke="#cfe3f5" stroke-width="3"/></svg>
  <svg class="abs arrow" style="right:40px" viewBox="0 0 24 30"><path d="M8,5 L17,15 L8,25" fill="none" stroke="#cfe3f5" stroke-width="3"/></svg>
  <h1 class="abs hero-title">SAILBUDDIES</h1>
  <p class="abs hero-text">Organize children who suffer from diseases or disabilities a week off on a Boat to give the children new hope and an unforgettable experience.</p>
  <a class="btn hero-btn">Get more info</a>
</section>

<section class="welcome">
  <div class="abs welcome-photo" role="img" aria-label="Child in a life jacket leaning on the bow of a white boat"></div>
  <h2 class="abs section-title welcome-title">Welcome to<br>Sailbuddies</h2>
  <p class="abs welcome-text">We are trained social educators and experienced skippers who volunteer in the Sailbuddies association and organize a fleet every year for socially disadvantaged children and young people from the Upper Austrian central area and set up the necessary financial resources for this.</p>
  <a class="btn welcome-btn">Read more</a>
</section>

<section class="sponsors">
  <svg class="abs sponsor-band" width="1200" height="586" viewBox="0 1240 1200 586">
    <path d="M0,1345 C300,1420 560,1262 860,1245 C1010,1238 1120,1268 1200,1300 L1200,1826 L0,1826Z" fill="var(--pale)"/>
  </svg>
  <h2 class="abs section-title sponsor-title">Our<br>Sponsors</h2>
  <a class="btn sponsor-btn">View more</a>
  <div class="abs sponsor-grid">
    <div class="sponsor-card">Lindmair Bau</div>
    <div class="sponsor-card">Brunnhof Werk</div>
    <div class="sponsor-card">Elektro Sternau</div>
    <div class="sponsor-card">Wellental Reisen</div>
    <div class="sponsor-card">SV Feldau</div>
    <div class="sponsor-card">Marivo Group</div>
    <div class="sponsor-card">Hofbrunner</div>
    <div class="sponsor-card">Felsgarten Stein</div>
    <div class="sponsor-card">Kraftwerk Kids</div>
  </div>
</section>

<section class="fleet">
  <div class="abs fleet-photo" role="img" aria-label="White sailing yacht under full sail on the open sea"></div>
  <h2 class="abs section-title fleet-title" style="color:var(--white)">Fleet information 2022</h2>
  <p class="abs fleet-lead">The 2022 fleet will be held and will take place from 28. August to 03. September.</p>
  <p class="abs fleet-text">Nemo enim ipsam voluptatem quia voluptas sit aspernatur ut odit aut fugit, sed quia consequuntur magni dolores eos qui rt ione voluptatem sequi nesciunt. Neque porro quisquam est, qui dolorem ipsum quia dolor sit amet, consectetur, adipisci velit, sed quia non numquam eius.</p>
  <a class="btn fleet-btn">Read more</a>
</section>

<section class="gallery">
  <h2 class="abs section-title gallery-title">Gallery</h2>
  <div class="abs gallery-grid">
    <div class="gallery-item g1" role="img" aria-label="Two boys in green shirts laughing by the water"></div>
    <div class="gallery-item g2" role="img" aria-label="Children in orange life jackets in a small sailboat"></div>
    <div class="gallery-item g3" role="img" aria-label="Children sitting on the deck of a yacht"></div>
    <div class="gallery-item g4" role="img" aria-label="Yacht deck and mast at sunset"></div>
    <div class="gallery-item g5" role="img" aria-label="Young sailor in a dinghy on sparkling water"></div>
    <div class="gallery-item g6" role="img" aria-label="Smiling girl holding a rope on a boat"></div>
  </div>
  <a class="btn gallery-btn">View more</a>
</section>

<footer>
  <svg class="abs footer-waves" width="1200" height="600" viewBox="0 3340 1200 600">
    <path d="M0,3525 C200,3410 420,3470 700,3495 C950,3515 1100,3430 1200,3350" fill="none" stroke="#00a9dd" stroke-width="8"/>
    <path d="M0,3545 C200,3430 420,3485 700,3510 C950,3530 1100,3450 1200,3375 L1200,3400 C1100,3470 950,3545 700,3525 C420,3500 200,3450 0,3565Z" fill="#c7ebf8"/>
    <path d="M0,3565 C200,3450 420,3500 700,3525 C950,3545 1100,3470 1200,3400 L1200,3940 L0,3940Z" fill="var(--footer)"/>
  </svg>
  <div class="abs footer-brand"><span class="dot"></span>Sailbuddies</div>
  <div class="abs footer-col quick">
    <h3>Quick Links</h3>
    <ul><li>Home</li><li>About</li><li>Sponsors</li><li>Fleet information 2022</li><li>Gallery</li><li>Contact</li></ul>
  </div>
  <div class="abs footer-col contact">
    <h3>Contact Us</h3>
    <ul>
      <li><svg width="12" height="15" viewBox="0 0 12 15"><path d="M6,0C2.7,0 0,2.6 0,5.8C0,10 6,15 6,15C6,15 12,10 12,5.8C12,2.6 9.3,0 6,0Z" fill="#fff"/><circle cx="6" cy="5.8" r="2.2" fill="var(--footer)"/></svg><span>No: 1234 Sed ut patis unde omnis<br>iste natus error sit volu</span></li>
      <li><svg width="14" height="14" viewBox="0 0 14 14"><path d="M3,0L5.5,3.5L4,5.2C5,7.2 6.8,9 8.8,10L10.5,8.5L14,11L12.5,13.5C7,14 0,7 0.5,1.5Z" fill="#fff"/></svg><span>1 888 888 8888</span></li>
      <li><svg width="16" height="12" viewBox="0 0 16 12"><rect width="16" height="12" rx="1.5" fill="#fff"/><path d="M1,1.5L8,7L15,1.5" fill="none" stroke="var(--footer)" stroke-width="1.4"/></svg><span>info@sailbuddies.com</span></li>
    </ul>
  </div>
  <div class="abs footer-rule"></div>
  <p class="abs copyright">Copyright © 2022, Sailbuddies. All rights reserved.</p>
  <div class="abs social">
    <span aria-label="Social profile one"></span>
    <span aria-label="Social profile two"></span>
    <span aria-label="Social profile three"></span>
    <span aria-label="Email"><svg width="18" height="13" viewBox="0 0 16 12"><rect width="16" height="12" rx="1.5" fill="#00a9dd"/><path d="M1,1.5L8,7L15,1.5" fill="none" stroke="var(--footer)" stroke-width="1.4"/></svg></span>
  </div>
</footer>

</body>
</html>
```